Global Leadership Company requires banner design

I need 3 large banners designed. i will be using these for advertising and also a condensed version as the header on a splash pages.

I have attached the wording and also the photo's that i'd like used in each design.
Note: i've just placed the wording randomly, you'll have to place it where it makes the most sense for the message and the design.

I want something with bright colors that pops.

Reason: I'd like to give the most recent designers time to submit quality work.

```html
<!DOCTYPE html>
<html lang="en">
<head>
<meta charset="utf-8">
<title>Leadership Banners</title>
<link rel="stylesheet" href="https://fonts.googleapis.com/css2?family=Oswald:wght@500;600&family=Open+Sans:ital,wght@0,400;0,600;1,400&display=swap">
<style>
  :root {
    --sheet-bg: #0b0b0b;
    --blue-a: #1a2de6;
    --blue-b: #2f78f2;
    --red-a: #f0661e;
    --red-b: #e8141c;
    --pill: #fbf1c4;
    --ink: #14141a;
    --white: #ffffff;
    --btn-a: #fff45a;
    --btn-b: #ffd400;
    --box-blue: rgba(4, 18, 110, 0.55);
    --box-red: rgba(130, 0, 0, 0.45);
  }
  * { margin: 0; padding: 0; box-sizing: border-box; }
  html, body { width: 1200px; height: 643px; overflow: hidden; background: var(--sheet-bg); }
  body { position: relative; font-family: "Open Sans", Arial, sans-serif; color: var(--white); }

  .banner { position: absolute; height: 170px; overflow: hidden; }
  .col-left { left: 25px; width: 557px; }
  .col-right { left: 598px; width: 569px; }
  .row-1 { top: 62px; }
  .row-2 { top: 240px; }
  .row-3 { top: 424px; }
  .theme-blue { background: linear-gradient(90deg, var(--blue-a), var(--blue-b)); }
  .theme-red { background: linear-gradient(90deg, var(--red-a), var(--red-b)); }
  .theme-blue .quote-box, .theme-blue .note-box { background: var(--box-blue); }
  .theme-red .quote-box, .theme-red .note-box { background: var(--box-red); }

  .headline {
    position: absolute; left: 50%; transform: translateX(-50%);
    background: var(--pill); color: var(--ink); border-radius: 8px;
    font-family: "Oswald", "Arial Narrow", sans-serif; font-weight: 600;
    text-transform: uppercase; white-space: nowrap; padding: 0 8px;
    box-shadow: 0 0 0 2px rgba(0,0,0,.15);
  }
  .row-1 .headline { top: 12px; font-size: 20px; line-height: 27px; }
  .row-2 .headline { top: 3px; font-size: 17px; line-height: 25px; }
  .row-3 .headline { top: 6px; font-size: 19px; line-height: 27px; }

  .photo { position: absolute; border: 3px solid var(--white); }
  .photo-round { left: 10px; top: 35px; width: 102px; height: 102px; border-radius: 50%;
    background: radial-gradient(circle at 50% 40%, #d9b98a, #7a5a3a 70%, #3a2a1a); }
  .row-2 .photo { left: 12px; top: 32px; width: 122px; height: 118px;
    background: linear-gradient(135deg, #2a2a30, #6b5a4a 55%, #c9a57a); }
  .row-3 .photo { left: 2px; top: 27px; width: 136px; height: 117px;
    background: linear-gradient(135deg, #0d0d10, #3c2a20 55%, #a88460); }

  .note-box { position: absolute; left: 108px; top: 50px; width: 214px; height: 70px;
    padding: 6px 0 0 8px; font-size: 12.5px; line-height: 19px; }
  .note-box .who { display: block; }

  .quote-box { position: absolute; font-size: 16px; line-height: 20px; }
  .row-1 .quote-box { left: 322px; top: 44px; width: 240px; padding: 0 5px; background: none; }
  .row-2 .quote-box { left: 324px; top: 43px; width: 240px; height: 90px; padding: 4px 6px; }
  .row-3 .quote-box { left: 312px; top: 40px; width: 252px; padding: 5px 6px;
    font-size: 13.3px; line-height: 20px; letter-spacing: -0.2px; }

  .tagline { position: absolute; font-style: italic; font-size: 12.5px; }
  .row-1 .tagline { left: 112px; top: 140px; }
  .bullets { position: absolute; left: 138px; top: 55px; width: 180px; font-size: 10.5px; line-height: 14px; }
  .bullets p + p { margin-top: 12px; }
  .pitch { position: absolute; left: 140px; top: 60px; width: 155px; font-size: 12.5px; line-height: 15px; }

  .footer-line { position: absolute; font-style: italic; font-size: 11px; word-spacing: 2px; white-space: nowrap; }
  .row-2 .footer-line { left: 15px; top: 154px; }
  .row-3 .footer-line { left: 8px; top: 152px; }
  .footer-line span { margin-right: 18px; }

  .cta { position: absolute; width: 133px; height: 27px; border-radius: 6px;
    background: linear-gradient(180deg, var(--btn-a), var(--btn-b)); border: 1px solid #b89400;
    display: flex; align-items: center; justify-content: center; gap: 8px;
    font-family: "Oswald", "Arial Narrow", sans-serif; font-weight: 600; font-size: 16px;
    line-height: 1; white-space: nowrap; color: var(--ink); text-decoration: none; }
  .cta svg { flex: none; }
  .row-1 .cta { left: 327px; top: 134px; }
  .row-2 .cta { left: 323px; top: 140px; }
  .row-3 .cta { left: 313px; top: 138px; }
</style>
</head>
<body>

<section class="banner row-1 col-left theme-blue">
  <h2 class="headline">Want to make $25,000 per month?</h2>
  <div class="photo photo-round" role="img" aria-label="Portrait of a smiling woman with blonde hair"></div>
  <p class="note-box">“Within just 5 months I was making over $25,000 per month”<span class="who">Dana, Colorado</span></p>
  <p class="quote-box">“Let us show you how we’ve taught average people to earn an executives salary from home part time. FAST!”</p>
  <p class="tagline">Just launched in United States</p>
  <a class="cta" href="#">CLICK HERE <svg width="40" height="18" viewBox="0 0 40 18"><path d="M2 1l9 8-9 8h7l9-8-9-8zM14 1l9 8-9 8h7l9-8-9-8zM26 1l9 8-9 8h5l8-8-8-8z" fill="#14141a"/></svg></a>
</section>

<section class="banner row-1 col-right theme-red">
  <h2 class="headline">Want to make $25,000 per month?</h2>
  <div class="photo photo-round" role="img" aria-label="Portrait of a smiling woman with blonde hair"></div>
  <p class="note-box">“Within just 5 months I was making over $25,000 per month”<span class="who">Dana, Colorado</span></p>
  <p class="quote-box">“Let us show you how we’ve taught average people to earn an executives salary from home part time. FAST!”</p>
  <p class="tagline">Just launched in United States</p>
  <a class="cta" href="#">CLICK HERE <svg width="40" height="18" viewBox="0 0 40 18"><path d="M2 1l9 8-9 8h7l9-8-9-8zM14 1l9 8-9 8h7l9-8-9-8zM26 1l9 8-9 8h5l8-8-8-8z" fill="#14141a"/></svg></a>
</section>

<section class="banner row-2 col-left theme-red">
  <h2 class="headline">Passionate about personal development / leadership development?</h2>
  <div class="photo" role="img" aria-label="Photo of a couple in formal wear at an evening event"></div>
  <div class="bullets"><p>-Looking to align yourself with an opportunity of substance?</p><p>-Ready to be challenged &amp; encouraged to reach new level’s of success</p></div>
  <p class="quote-box">“Let us show you how we’ve taught others like you to make a quantum leap in their personal results”</p>
  <p class="footer-line"><span>- Home Based</span><span>- NOT MLM</span>- No Cold Calling</p>
  <a class="cta" href="#">CLICK HERE <svg width="40" height="18" viewBox="0 0 40 18"><path d="M2 1l9 8-9 8h7l9-8-9-8zM14 1l9 8-9 8h7l9-8-9-8zM26 1l9 8-9 8h5l8-8-8-8z" fill="#14141a"/></svg></a>
</section>

<section class="banner row-2 col-right theme-blue">
  <h2 class="headline">Passionate about personal development / leadership development?</h2>
  <div class="photo" role="img" aria-label="Photo of a couple in formal wear at an evening event"></div>
  <div class="bullets"><p>-Looking to align yourself with an opportunity of substance?</p><p>-Ready to be challenged &amp; encouraged to reach new level’s of success</p></div>
  <p class="quote-box">“Let us show you how we’ve taught others like you to make a quantum leap in their personal results”</p>
  <p class="footer-line"><span>- Home Based</span><span>- NOT MLM</span>- No Cold Calling</p>
  <a class="cta" href="#">CLICK HERE <svg width="40" height="18" viewBox="0 0 40 18"><path d="M2 1l9 8-9 8h7l9-8-9-8zM14 1l9 8-9 8h7l9-8-9-8zM26 1l9 8-9 8h5l8-8-8-8z" fill="#14141a"/></svg></a>
</section>

<section class="banner row-3 col-left theme-blue">
  <h2 class="headline">Change your tomorrow – today!</h2>
  <div class="photo" role="img" aria-label="Photo of a smiling couple at night"></div>
  <p class="pitch">Learn our success formula today so you can enjoy more tomorrow</p>
  <p class="quote-box">Learn to turn your spare time into an executive level income.<br>In just 2 hours per day you can make a quantum leap in your results.</p>
  <p class="footer-line"><span>more time</span><span>more fulfillment</span><span>more money</span>more fun</p>
  <a class="cta" href="#">CLICK HERE <svg width="40" height="18" viewBox="0 0 40 18"><path d="M2 1l9 8-9 8h7l9-8-9-8zM14 1l9 8-9 8h7l9-8-9-8zM26 1l9 8-9 8h5l8-8-8-8z" fill="#14141a"/></svg></a>
</section>

<section class="banner row-3 col-right theme-red">
  <h2 class="headline">Change your tomorrow – today!</h2>
  <div class="photo" role="img" aria-label="Photo of a smiling couple at night"></div>
  <p class="pitch">Learn our success formula today so you can enjoy more tomorrow</p>
  <p class="quote-box">Learn to turn your spare time into an executive level income.<br>In just 2 hours per day you can make a quantum leap in your results.</p>
  <p class="footer-line"><span>more time</span><span>more fulfillment</span><span>more money</span>more fun</p>
  <a class="cta" href="#">CLICK HERE <svg width="40" height="18" viewBox="0 0 40 18"><path d="M2 1l9 8-9 8h7l9-8-9-8zM14 1l9 8-9 8h7l9-8-9-8zM26 1l9 8-9 8h5l8-8-8-8z" fill="#14141a"/></svg></a>
</section>

</body>
</html>
```